Communication Coach needs a business card

https://imgvault-example.net/gallery/1839201/40417/40417_22719043_1839201_8c3e7b2f_preview.png

I like this a lot

I want it to include the following

Delia Strennick
M.A.CCC-SLP
555-204-7718
delia.strennick@mailvento.net
Communication Trainer and Executive Function Coaching
Be Confident-Be Authentic- Be Memorable

on back of card
Public Speaking
Executive Function Coaching
Interview Skills
Corporate Workshops
Self Regulation/Confidence Building

Target Market(s)

adults, parents

Contact Information for Business Card

See above description. i included picture of what i like

Requirements
Must have
• two sides, multi colors ,double sided
Nice to have
• I could have a tag line on front such as Be confident-Be memorable -Be authentic
Should not have
• not too busy or creative as needs to work for corporate setting

```html
<!DOCTYPE html>
<html lang="en">
<head>
<meta charset="utf-8">
<title>Delia Strennick – Business Card</title>
<link href="https://fonts.googleapis.com/css2?family=Cinzel:wght@400;500&family=Dancing+Script:wght@700&family=Poppins:wght@400;500&display=swap" rel="stylesheet">
<style>
  :root{
    --bg:#d3d3d3;
    --ink:#1e1e1e;
    --white:#ffffff;
    --purple:#8e56a4;
    --yellow:#f2d543;
    --pink:#ef5f73;
    --teal:#37b1a8;
    --green:#97c94c;
    --orange:#f07c58;
  }
  *{margin:0;padding:0;box-sizing:border-box}
  html,body{width:1200px;height:900px;overflow:hidden}
  body{background:var(--bg);position:relative;font-family:"Poppins",sans-serif}

  .card{position:absolute;left:250px;width:700px;height:400px;border-radius:34px;overflow:hidden;
        box-shadow:0 6px 14px rgba(0,0,0,.25)}
  .card-back{top:35px;display:flex}
  .card-front{top:465px;background:var(--ink)}

  /* back side stripes */
  .stripe{height:100%;display:flex;align-items:center;justify-content:center}
  .stripe-edge{width:58px}
  .stripe-service{flex:1}
  .service{writing-mode:vertical-rl;transform:rotate(180deg);color:var(--white);font-weight:500;
           font-size:17px;letter-spacing:.5px;text-transform:uppercase;text-align:center;line-height:1.25;max-height:340px}

  .purple{background:var(--purple)} .yellow{background:var(--yellow)} .pink{background:var(--pink)}
  .teal{background:var(--teal)} .green{background:var(--green)} .orange{background:var(--orange)}

  /* front side */
  .color-band{position:absolute;left:0;width:100%;height:46px;display:flex}
  .color-band span{flex:1}
  .color-band-top{top:0}
  .color-band-bottom{bottom:0}

  .front-text{position:absolute;color:var(--white)}
  .title{left:90px;top:72px;font-family:"Cinzel",serif;font-size:23px;line-height:1.05;letter-spacing:1px;font-weight:400}
  .title .indent{display:block;padding-left:150px}
  .tagline{left:190px;top:134px;font-size:14.5px;font-weight:500;letter-spacing:.3px}

  .signature{position:absolute;left:0;top:180px;width:700px;height:100px;display:flex;align-items:center}
  .signature-line-left{flex:0 0 200px;height:100px}
  .signature-line-right{flex:1;height:100px}
  .name{font-family:"Dancing Script","Brush Script MT",cursive;font-weight:700;font-size:58px;line-height:1;
        color:var(--white);white-space:nowrap;padding:0 6px 0 2px}

  .credential{left:430px;top:270px;font-size:15px;letter-spacing:.5px}
  .contact{left:222px;top:310px;font-size:16px;letter-spacing:.3px;white-space:nowrap}
</style>
</head>
<body>

<section class="card card-back" aria-label="Back of card: services">
  <div class="stripe stripe-edge purple"></div>
  <div class="stripe stripe-service yellow"><p class="service">Public Speaking</p></div>
  <div class="stripe stripe-service pink"><p class="service">Executive Function<br>Coaching</p></div>
  <div class="stripe stripe-service teal"><p class="service">Interview Skills</p></div>
  <div class="stripe stripe-service green"><p class="service">Corporate&nbsp; Workshops</p></div>
  <div class="stripe stripe-service orange"><p class="service">Self Regulation/<br>Confidence Building</p></div>
  <div class="stripe stripe-edge purple"></div>
</section>

<section class="card card-front" aria-label="Front of card: contact details">
  <div class="color-band color-band-top">
    <span class="purple"></span><span class="yellow"></span><span class="pink"></span>
    <span class="teal"></span><span class="green"></span><span class="orange"></span>
  </div>

  <h1 class="front-text title">Communication Trainer and Executive<span class="indent">Function Coaching</span></h1>
  <p class="front-text tagline">Be Confident-Be Authentic- Be Memorable</p>

  <div class="signature">
    <svg class="signature-line-left" viewBox="0 0 200 100" preserveAspectRatio="none" aria-hidden="true">
      <path d="M20 99 Q120 82 200 62" stroke="#fff" stroke-width="2.5" fill="none" stroke-linecap="round"/>
    </svg>
    <p class="name">Delia Strennick</p>
    <svg class="signature-line-right" viewBox="0 0 100 100" preserveAspectRatio="none" aria-hidden="true">
      <path d="M0 62 Q50 40 100 12" stroke="#fff" stroke-width="2.5" fill="none" stroke-linecap="round" vector-effect="non-scaling-stroke"/>
    </svg>
  </div>

  <p class="front-text credential">M.A.CCC-SLP</p>
  <p class="front-text contact">555-204-7718 | delia.strennick@mailvento.net</p>

  <div class="color-band color-band-bottom">
    <span class="purple"></span><span class="yellow"></span><span class="pink"></span>
    <span class="teal"></span><span class="green"></span><span class="orange"></span>
  </div>
</section>

</body>
</html>
```